Website for Corvalind Capital, my new firm that raises money from investors to buy, build, own an...

Corvalind Capital needs a website! We are a new company with very experienced people, who invest in, own and build hotel properties, as well as apartments and other commercial real estate. We seek investors for our projects, and we provide safe, secure returns on their investment in our projects. Our new logo is designed to exhibit strength, class and security, and would like our website to continue on this theme. Our name, Corvalind, is a word-play on a Greek word “aristeia”, which means “excellence” and “a warriors finest moment of glory in war”. If you are in business, you realize that much of it is like war, with strategy and moves and opponents and competitors, and ever-changing economic conditions and threats that make business very much like war. We like to think that we are good at business (war), and so have named our company “Corvalind”, using the founders last name and the word “aristeia” combined. Another definition of "aristeia" is "performing at the peak of one's potential after a long struggle"...again, much like business in real life! The website design should exhibit financial security, smart moves, and positive growth towards a bright future.

Target Market(s)

The target market is smart and wealthy investors, with others such as brokers, cities and government agencies, lenders, sellers, partners, etc also looking at it.

Industry/Entity Type

Investment

Number of Pages Required

5+ page

Font styles to use
Sans Serif

Colors
fec214

Requirements
Must have
• Our website should have a landing page, a "about" or bio page, a projects page and a contact us page. Our new logo uses the colors black and gold, so this should be factored in to our site. The site should be simple, yet impactful and impressive. I have actually two logos, which can be mixed and interchanged in a complimentary way, each with their own unique look.
Nice to have
• I have uploaded a couple screenshots of a website i like, and the simplicity I mention.
Should not have
• The site should not be flashy or complicated or complex or "busy"

```html
<!DOCTYPE html>
<html lang="en">
<head>
<meta charset="utf-8">
<title>Corvalind Capital</title>
<link href="https://fonts.googleapis.com/css2?family=Domine:wght@400;700&family=Open+Sans:ital,wght@0,400;0,600;0,700;1,400;1,600&display=swap" rel="stylesheet">
<style>
:root{
  --gold:#f8b90f;
  --ink:#1b1b1b;
  --text:#333333;
  --paper:#ffffff;
  --blush:#f7f3f2;
  --footer:#1a1a1a;
  --line:#3a3a3a;
}
*{box-sizing:border-box;margin:0;padding:0}
html,body{width:1200px;height:2184px;overflow:hidden;background:var(--paper)}
body{position:relative;font-family:"Open Sans",Arial,sans-serif;color:var(--text)}
.abs{position:absolute}
.serif{font-family:"Domine",Georgia,serif}

/* hero */
.hero{left:0;top:0;width:1200px;height:641px;
  background:linear-gradient(90deg,#2b2f36 0%,#4a5058 22%,#7c8590 48%,#a9b3bd 52%,#596069 70%,#30343a 100%)}
.hero-shade{left:0;top:0;width:1200px;height:641px;
  background:linear-gradient(180deg,rgba(20,22,26,.25) 0%,rgba(20,22,26,.15) 50%,rgba(40,36,30,.55) 100%)}
.topbar{right:95px;top:10px;font-size:10px;color:#fff;display:flex;gap:36px;align-items:center}
.topbar span{display:flex;align-items:center;gap:6px}
.header{left:0;top:35px;width:1200px;height:87px;background:rgba(255,255,255,.93)}
.brand{left:131px;top:62px;display:flex;align-items:center;gap:8px;font-weight:700;font-size:17px;letter-spacing:1px;color:var(--ink)}
.brand i{display:block;width:12px;height:12px;background:var(--gold)}
.nav a{position:absolute;top:73px;font-size:14px;color:#333;text-decoration:none}
.nav .active::after{content:"";position:absolute;left:0;right:0;bottom:-14px;height:3px;background:var(--gold)}
.hero-title{left:131px;top:240px;font-size:50px;line-height:50px;font-weight:700;color:var(--gold)}
.hero-copy{left:131px;top:360px;width:445px;font-size:12.4px;line-height:16.5px;color:#fff}
.btn{display:flex;align-items:center;justify-content:center;border:2px solid var(--gold);font-size:13px;color:var(--ink)}
.hero-btn{left:131px;top:446px;width:118px;height:42px;color:#fff}

/* projects */
.projects{left:0;top:641px;width:1200px;height:604px;background:var(--blush)}
.eyebrow{left:0;width:1200px;top:664px;text-align:center;font-size:10px;letter-spacing:2px;color:#444}
.sec-title{width:1200px;left:0;text-align:center;font-size:29px;font-weight:700;color:var(--gold)}
.rule{height:2px;width:44px;background:var(--ink)}
.card{overflow:hidden}
.card .band{position:absolute;left:0;right:0;bottom:0;height:73px;background:rgba(10,10,10,.78);padding:10px 18px}
.card h3{font-family:"Domine",Georgia,serif;font-size:20px;color:var(--gold);font-weight:700;line-height:27px}
.card p{font-size:13px;color:#fff}
.card p b{color:var(--gold);font-weight:400}

/* about */
.about-photo{left:0;top:1274px;width:587px;height:368px;background:linear-gradient(135deg,#6d6a66 0%,#9b8f84 40%,#3f3c3c 75%,#2b2a2c 100%)}
.about-copy{left:609px;top:1361px;width:452px;font-size:12.4px;line-height:16px;color:#333}
.feature{width:130px;text-align:center}
.feature .ring{width:50px;height:50px;margin:0 auto;border:2px solid var(--gold);border-radius:50%;display:flex;align-items:center;justify-content:center}
.feature span{display:block;margin-top:18px;font-family:"Domine",Georgia,serif;font-size:14px;color:var(--ink)}

/* contact */
.contact-bg{left:0;top:1790px;width:1200px;height:346px;background:linear-gradient(180deg,#ffffff 0%,#eef2f6 60%,#e2e8ee 100%)}
.contact-lead{left:0;top:1738px;width:1200px;text-align:center;font-size:12.4px;line-height:16px;color:#333}
.sub-title{font-family:"Domine",Georgia,serif;font-size:19px;color:var(--gold)}
.info{left:133px;top:1848px;font-size:11px;color:#333}
.info li{list-style:none;display:flex;align-items:center;gap:14px;height:20.7px}
.info svg{width:12px;height:12px}
.follow{left:133px;top:1947px;font-size:14.5px;color:#222}
.social{left:133px;top:1994px;display:flex;gap:14px}
.social i{display:block;width:18px;height:18px;border-radius:50%;background:var(--ink)}
.field{border:1.5px solid var(--line);background:#fff;font-size:10px;font-style:italic;font-weight:600;color:#444;padding:9px 16px}
.send{left:948px;top:2067px;width:119px;height:41px;background:transparent}

/* footer */
.footer{left:0;top:2136px;width:1200px;height:48px;background:var(--footer);color:#fff;font-size:11px;font-style:italic;font-weight:600}
.footer span{position:absolute;top:17px}
</style>
</head>
<body>

<!-- hero -->
<div class="abs hero" role="img" aria-label="Photo of a busy downtown avenue lined with high-rise towers and yellow taxis"></div>
<div class="abs hero-shade"></div>
<div class="abs topbar">
  <span><svg width="12" height="9" viewBox="0 0 12 9"><rect width="12" height="9" fill="#fff"/><path d="M0 0l6 5 6-5" stroke="#333" fill="none"/></svg>info@corvalindcapital.com</span>
  <span><svg width="11" height="11" viewBox="0 0 24 24"><path fill="#fff" d="M6.6 10.8a15 15 0 006.6 6.6l2.2-2.2a1 1 0 011-.25 11.4 11.4 0 003.6.6 1 1 0 011 1V20a1 1 0 01-1 1A17 17 0 013 4a1 1 0 011-1h3.5a1 1 0 011 1c0 1.25.2 2.45.6 3.6a1 1 0 01-.25 1z"/></svg>+99 4410 2387 5</span>
</div>
<header class="abs header"></header>
<div class="abs brand"><i></i>CORVALIND</div>
<nav class="nav">
  <a class="active" href="#" style="left:408px">Home</a>
  <a href="#" style="left:521px">Projects</a>
  <a href="#" style="left:655px">About Us</a>
  <a href="#" style="left:779px">Contact Us</a>
  <svg class="abs" style="left:903px;top:73px" width="18" height="18" viewBox="0 0 18 18"><circle cx="10" cy="7" r="5.5" fill="none" stroke="#f8b90f" stroke-width="2"/><path d="M6 11l-4.5 4.5" stroke="#f8b90f" stroke-width="2.4"/></svg>
  <a href="#" style="left:957px">Search</a>
</nav>
<h1 class="abs hero-title serif">Lorem Ipsum Dolor<br>Sit Amet</h1>
<p class="abs hero-copy">Lorem ipsum dolor sit amet, consectetur adipiscing elit, sed do eiusmod tem por incididunt ut labore et dolore magna aliqua. Ut enim ad minim veniam, quis nostrud exercitation ullamco laboris nisi ut aliquip ex ea commod</p>
<div class="abs btn hero-btn">Read More</div>

<!-- projects -->
<section class="abs projects"></section>
<div class="abs eyebrow serif">EXPLORE OUR PROJECTS</div>
<h2 class="abs sec-title serif" style="top:672px">Projects</h2>
<div class="abs rule" style="left:578px;top:719px"></div>

<div class="abs card" style="left:131px;top:760px;width:456px;height:384px;background:linear-gradient(180deg,#4f79b3 0%,#9fb9d6 40%,#d9d7d2 65%,#6b5a4d 100%)" role="img" aria-label="Photo of a multi-storey hotel building">
  <div class="band"><h3>Hotels</h3><p><b>4</b> Properties</p></div>
</div>
<div class="abs card" style="left:607px;top:760px;width:460px;height:182px;background:linear-gradient(135deg,#7fa9d6 0%,#b7cfe6 40%,#3b3a38 70%,#cfc7bc 100%)" role="img" aria-label="Photo of a modern apartment block">
  <div class="band"><h3>Appartments</h3><p><b>5</b> Properties</p></div>
</div>
<div class="abs card" style="left:607px;top:961px;width:221px;height:183px;background:linear-gradient(180deg,#e8a33a 0%,#f3c35a 35%,#3d3a2e 70%,#2a2a25 100%)" role="img" aria-label="Photo of a house at sunset">
  <div class="band"><h3>Homes</h3><p><b>7</b> Properties</p></div>
</div>
<div class="abs card" style="left:844px;top:961px;width:223px;height:183px;background:linear-gradient(180deg,#4c6f99 0%,#8aa4bf 35%,#b07a52 65%,#3d3b2c 100%)" role="img" aria-label="Photo of a ranch house among palm trees">
  <div class="band"><h3>Farms</h3><p><b>2</b> Properties</p></div>
</div>
<div class="abs btn" style="left:537px;top:1175px;width:120px;height:41px">Read More</div>

<!-- about -->
<div class="abs about-photo" role="img" aria-label="Photo of a team of colleagues gathered around a laptop in an office"></div>
<h2 class="abs serif" style="left:609px;width:452px;top:1296px;text-align:center;font-size:29px;font-weight:700;color:var(--gold)">About Us</h2>
<div class="abs rule" style="left:765px;top:1341px;width:40px"></div>
<p class="abs about-copy">Lorem ipsum dolor sit amet, consectetur adipiscing elit, sed do eiusmotem por incididunt ut labore et dolore magna aliqua. Ut enim ad minim veniam, quis-nostrud exercitation ullamco laboris nisi ut aliquip ex ea commod rem ipsum dolor sit amet, consectetur adipiscing elit, sed do eiusmotem</p>

<div class="abs feature" style="left:618px;top:1450px"><div class="ring"><svg width="24" height="24" viewBox="0 0 24 24"><path d="M3 20h18M5 17v-3M9 17v-6M13 17v-4M17 17V9" stroke="#1b1b1b" stroke-width="2.4"/><path d="M4 11l5-5 4 3 6-6M15 3h4v4" stroke="#1b1b1b" stroke-width="2" fill="none"/></svg></div><span>Lorem Ipsum</span></div>
<div class="abs feature" style="left:774px;top:1450px"><div class="ring"><svg width="22" height="22" viewBox="0 0 24 24"><circle cx="12" cy="7" r="4.5" fill="#1b1b1b"/><path d="M3 22c0-6 4-9 9-9s9 3 9 9z" fill="#1b1b1b"/></svg></div><span>Lorem Ipsum</span></div>
<div class="abs feature" style="left:925px;top:1450px"><div class="ring"><svg width="22" height="22" viewBox="0 0 24 24"><path d="M6 21h12v-3H6zM8 17h8l-1-7 3-2-5-5-6 3v9z" fill="#1b1b1b"/></svg></div><span>Lorem Ipsum</span></div>
<div class="abs feature" style="left:624px;top:1555px"><div class="ring"><svg width="22" height="22" viewBox="0 0 24 24"><path d="M12 2l8 3v7c0 5-4 8-8 10-4-2-8-5-8-10V5z" fill="#1b1b1b"/><text x="12" y="16" font-size="11" fill="#fff" text-anchor="middle" font-family="Arial,sans-serif" font-weight="700">$</text></svg></div><span>Lorem Ipsum</span></div>
<div class="abs feature" style="left:772px;top:1555px"><div class="ring"><svg width="22" height="22" viewBox="0 0 24 24"><circle cx="14" cy="8" r="5.5" fill="#1b1b1b"/><text x="14" y="11.5" font-size="8" fill="#fff" text-anchor="middle" font-family="Arial,sans-serif" font-weight="700">$</text><path d="M2 15h5l5 2h6l3-2v3l-4 3H8l-6-2z" fill="#1b1b1b"/></svg></div><span>Lorem Ipsum</span></div>
<div class="abs feature" style="left:928px;top:1555px"><div class="ring"><svg width="24" height="22" viewBox="0 0 26 24"><circle cx="13" cy="7" r="3.5" fill="#1b1b1b"/><circle cx="6" cy="9" r="2.8" fill="#1b1b1b"/><circle cx="20" cy="9" r="2.8" fill="#1b1b1b"/><path d="M7 20c0-5 3-8 6-8s6 3 6 8zM1 18c0-3 2-5 5-5s3 1 3 1l-2 4zM25 18c0-3-2-5-5-5s-3 1-3 1l2 4z" fill="#1b1b1b"/></svg></div><span>Lorem Ipsum</span></div>

<!-- contact -->
<div class="abs contact-bg" role="img" aria-label="Faint photo of a glass office tower rising behind the contact area"></div>
<h2 class="abs sec-title serif" style="top:1685px">Contact Us</h2>
<p class="abs contact-lead">Lorem ipsum dolor sit amet, consectetur adipiscing elit,<br>sed do eiusmod tempor incididunt ut</p>

<h3 class="abs sub-title" style="left:133px;top:1796px">Stay In Our Touch</h3>
<ul class="abs info">
  <li><svg viewBox="0 0 24 24"><path d="M12 2a7 7 0 00-7 7c0 5 7 13 7 13s7-8 7-13a7 7 0 00-7-7zm0 9.5A2.5 2.5 0 1112 6.5a2.5 2.5 0 010 5z" fill="#1b1b1b"/></svg>E218 , Westbrook ,  USA</li>
  <li><svg viewBox="0 0 24 24"><rect x="1" y="5" width="22" height="15" fill="#1b1b1b"/><path d="M1 5l11 8 11-8" stroke="#fff" stroke-width="1.6" fill="none"/></svg>info@corvalindcapital.com</li>
  <li><svg viewBox="0 0 24 24"><path fill="#1b1b1b" d="M6.6 10.8a15 15 0 006.6 6.6l2.2-2.2a1 1 0 011-.25 11.4 11.4 0 003.6.6 1 1 0 011 1V20a1 1 0 01-1 1A17 17 0 013 4a1 1 0 011-1h3.5a1 1 0 011 1c0 1.25.2 2.45.6 3.6a1 1 0 01-.25 1z"/></svg>+99 4410 2387 5</li>
  <li><svg viewBox="0 0 24 24"><rect x="2" y="8" width="20" height="14" fill="#1b1b1b"/><rect x="6" y="2" width="12" height="8" fill="#1b1b1b"/><rect x="6" y="12" width="12" height="3" fill="#fff"/></svg>+99 4410 2387 5</li>
</ul>
<div class="abs follow">Follow us</div>
<div class="abs social" aria-label="Social links"><i></i><i></i><i></i></div>

<h3 class="abs sub-title" style="left:609px;top:1790px">Contact Form</h3>
<div class="abs field" style="left:609px;top:1852px;width:214px;height:32px">Name</div>
<div class="abs field" style="left:850px;top:1852px;width:217px;height:32px">Email</div>
<div class="abs field" style="left:609px;top:1900px;width:458px;height:32px">Subject</div>
<div class="abs field" style="left:609px;top:1948px;width:458px;height:89px">Message</div>
<div class="abs btn send">Send</div>

<!-- footer -->
<footer class="abs footer">
  <span style="left:133px">Copyright by Corvalind Capital . All Right Reserved © 2018</span>
  <span style="left:798px">Client Support</span>
  <span style="left:901px">Privacy Policy</span>
  <span style="left:1002px">Terms of Use</span>
</footer>

</body>
</html>
```